New Poster Design Project

Need to create 1 letter size poster to advertise work shop series for people 55+. Description and poster content is in the attached word doc. Graphic of the book that the workshops are based on is also attached. Overall poster design should keep the same design aesthetic as the book cover.

```html
<!DOCTYPE html>
<html lang="en">
<head>
<meta charset="utf-8">
<title>Tech Savvy at Any Age – Speaker Series Poster</title>
<link href="https://fonts.googleapis.com/css2?family=Libre+Caslon+Display&family=Libre+Caslon+Text:ital,wght@0,400;0,700;1,400;1,700&family=Oswald:wght@500&family=Poppins:wght@400;500;600&display=swap" rel="stylesheet">
<style>
  :root {
    --backdrop: #404040;
    --sage: #7f997a;
    --forest: #2f4f2a;
    --cream: #f8efea;
    --orange: #e0622d;
    --peach: #f5cfa0;
    --brown: #8a4a1f;
    --ink: #1f1f1f;
    --label: #4f6b49;
    --white: #fbf7f2;
  }
  * { box-sizing: border-box; margin: 0; padding: 0; }
  html, body { width: 1011px; height: 1200px; overflow: hidden; background: var(--backdrop); }
  .poster {
    position: absolute; left: 99px; top: 76px; width: 805px; height: 1041px;
    background: var(--cream); overflow: hidden;
    font-family: "Poppins", sans-serif;
  }
  .sidebar { position: absolute; left: 0; top: 0; width: 355px; height: 100%; background: var(--sage); }
  .title {
    position: absolute; left: 36px; top: 22px; color: var(--white);
    font-family: "Libre Caslon Display", serif; font-weight: 400; line-height: 0.92;
  }
  .title .line1 { display: block; font-size: 64px; }
  .title .line2 { display: block; font-size: 64px; padding-left: 8px; }
  .title .small { font-size: 46px; vertical-align: 14px; }
  .series-band {
    position: absolute; left: 0; top: 177px; width: 355px; height: 176px; background: var(--forest);
  }
  .series-band .notch { position: absolute; left: 43px; top: -1px; width: 38px; height: 14px; }
  .series-text {
    position: absolute; left: 40px; top: 30px; color: var(--peach);
    font-family: "Libre Caslon Text", serif; font-style: italic; font-weight: 700; line-height: 1.2;
    font-size: 26px;
  }
  .series-text .for { font-size: 20px; font-weight: 400; }
  .series-text .audience { display: block; font-size: 50px; margin-top: 4px; line-height: 1; }
  .series-text .plus { font-style: normal; font-weight: 400; font-size: 36px; }
  .intro {
    position: absolute; left: 40px; top: 377px; width: 292px;
    color: var(--white); font-size: 16.2px; line-height: 21.6px;
  }
  .intro p + p { margin-top: 11px; }
  .sessions { position: absolute; left: 40px; top: 700px; width: 293px; height: 284px; }
  .sessions .rule-v { position: absolute; left: 139px; top: 0; width: 1px; height: 284px; background: rgba(255,255,255,0.6); }
  .sessions .rule-h { position: absolute; left: 0; width: 293px; height: 1px; background: rgba(255,255,255,0.6); }
  .session { position: absolute; width: 140px; }
  .session-pill {
    display: inline-flex; align-items: center; gap: 5px; height: 24px; padding: 0 16px 0 5px;
    background: var(--orange); border-radius: 12px; color: var(--white); font-size: 15px; font-weight: 500;
  }
  .session-pill svg { width: 16px; height: 16px; }
  .session-name { color: var(--white); font-size: 15.5px; font-weight: 500; line-height: 20.6px; margin-top: 3px; padding-left: 3px; letter-spacing: 0.2px; white-space: nowrap; }
  .tagline {
    position: absolute; left: 395px; top: 38px; color: var(--label);
    font-family: "Libre Caslon Display", serif; font-weight: 400; font-size: 30px; line-height: 35px;
    white-space: nowrap;
  }
  .scene-art {
    position: absolute; left: 355px; top: 142px; width: 450px; height: 286px;
    background: linear-gradient(135deg, #f8ebe2 0%, #f2cc93 45%, #e07a3e 70%, #8a4a2a 100%);
  }
  .books-badge { position: absolute; left: 676px; top: 337px; width: 104px; height: 104px; }
  .books-badge text { font-family: "Oswald", sans-serif; font-weight: 500; fill: var(--white); font-size: 18px; text-anchor: middle; }
  .details { position: absolute; left: 398px; top: 450px; width: 385px; }
  .detail-row { position: absolute; left: 0; width: 385px; }
  .detail-label { position: absolute; left: 0; top: 0; color: var(--label); font-size: 16px; font-weight: 500; }
  .detail-fill { position: absolute; left: 80px; top: 14px; width: 300px; border-top: 1px dashed #9a9a9a; }
  .detail-value { position: absolute; left: 73px; top: 2px; width: 318px; color: var(--ink); font-size: 13.2px; line-height: 14.6px; }
  .testimonials-heading {
    position: absolute; left: 392px; top: 651px; width: 361px; height: 37px;
    background: var(--forest); border-radius: 19px; color: var(--peach);
    font-size: 20px; font-weight: 600; text-align: center; line-height: 37px;
  }
  .quote { position: absolute; width: 162px; height: 65px; }
  .quote-box {
    position: absolute; left: 0; top: 0; width: 162px; height: 65px;
    border: 1px solid var(--forest); border-radius: 11px; background: var(--cream);
    padding: 12px 8px 0 27px; font-family: "Libre Caslon Text", serif; font-style: italic;
    font-size: 12px; line-height: 14.6px; color: var(--ink);
  }
  .quote-mark { position: absolute; left: -16px; top: 16px; width: 33px; height: 33px; }
  .presenter {
    position: absolute; left: 335px; top: 880px; width: 470px; height: 132px;
    background: var(--brown); border-radius: 23px 0 0 23px;
  }
  .presenter-text { position: absolute; left: 33px; top: 10px; width: 298px; color: var(--peach); font-family: "Libre Caslon Text", serif; font-style: italic; }
  .presenter-name { font-size: 17px; line-height: 22px; }
  .presenter-bio { font-size: 10.8px; line-height: 14.3px; font-weight: 400; letter-spacing: -0.1px; }
  .presenter-photo {
    position: absolute; left: 672px; top: 864px; width: 124px; height: 177px;
    border-radius: 56px 56px 0 0;
    background: linear-gradient(180deg, #e9b9a3 0%, #c98d78 45%, #2a2a2e 70%, #1d1d20 100%);
  }
</style>
</head>
<body>
<main class="poster">
  <section class="sidebar">
    <h1 class="title"><span class="line1">Tech Savvy</span><span class="line2"><span class="small">at</span> Any Age</span></h1>

    <div class="series-band">
      <svg class="notch" viewBox="0 0 38 14" aria-hidden="true"><polygon points="0,0 38,0 19,14" fill="#7f997a"/></svg>
      <p class="series-text">A 6-Part Community<br>Speaker Series <span class="for">for</span><span class="audience">Adults 55<span class="plus">+</span></span></p>
    </div>

    <div class="intro">
      <p>Technology plays an increasingly important role in staying connected, informed, and independent. This welcoming speaker series helps older adults better understand today’s digital tools, build confidence, and make informed decisions in everyday life.</p>
      <p>Sessions are practical, respectful, and discussion-friendly, with real-world examples and plenty of time for questions. No technical experience is required.</p>
    </div>

    <div class="sessions">
      <div class="rule-v"></div>
      <div class="rule-h" style="top:83px"></div>
      <div class="rule-h" style="top:196px"></div>

      <div class="session" style="left:0;top:0">
        <span class="session-pill"><svg viewBox="0 0 16 16" aria-hidden="true"><circle cx="8" cy="8" r="6.5" fill="none" stroke="#fbf7f2" stroke-width="1.2"/><path d="M5 8.2l2 2 4-4" fill="none" stroke="#fbf7f2" stroke-width="1.2"/></svg>Session 1</span>
        <p class="session-name">Foundations<br>of Technology</p>
      </div>
      <div class="session" style="left:160px;top:0">
        <span class="session-pill"><svg viewBox="0 0 16 16" aria-hidden="true"><circle cx="8" cy="8" r="6.5" fill="none" stroke="#fbf7f2" stroke-width="1.2"/><path d="M5 8.2l2 2 4-4" fill="none" stroke="#fbf7f2" stroke-width="1.2"/></svg>Session 2</span>
        <p class="session-name">Staying<br>connected</p>
      </div>
      <div class="session" style="left:0;top:96px">
        <span class="session-pill"><svg viewBox="0 0 16 16" aria-hidden="true"><circle cx="8" cy="8" r="6.5" fill="none" stroke="#fbf7f2" stroke-width="1.2"/><path d="M5 8.2l2 2 4-4" fill="none" stroke="#fbf7f2" stroke-width="1.2"/></svg>Session 3</span>
        <p class="session-name">Health and<br>Wellness</p>
      </div>
      <div class="session" style="left:159px;top:96px">
        <span class="session-pill"><svg viewBox="0 0 16 16" aria-hidden="true"><circle cx="8" cy="8" r="6.5" fill="none" stroke="#fbf7f2" stroke-width="1.2"/><path d="M5 8.2l2 2 4-4" fill="none" stroke="#fbf7f2" stroke-width="1.2"/></svg>Session 4</span>
        <p class="session-name">Enhancing<br>Independence<br>and Safety</p>
      </div>
      <div class="session" style="left:0;top:211px">
        <span class="session-pill"><svg viewBox="0 0 16 16" aria-hidden="true"><circle cx="8" cy="8" r="6.5" fill="none" stroke="#fbf7f2" stroke-width="1.2"/><path d="M5 8.2l2 2 4-4" fill="none" stroke="#fbf7f2" stroke-width="1.2"/></svg>Session 5</span>
        <p class="session-name">Emerging<br>Technologies</p>
      </div>
      <div class="session" style="left:156px;top:209px">
        <span class="session-pill"><svg viewBox="0 0 16 16" aria-hidden="true"><circle cx="8" cy="8" r="6.5" fill="none" stroke="#fbf7f2" stroke-width="1.2"/><path d="M5 8.2l2 2 4-4" fill="none" stroke="#fbf7f2" stroke-width="1.2"/></svg>Session 6</span>
        <p class="session-name">Practical Tools</p>
      </div>
    </div>
  </section>

  <h2 class="tagline">Navigating Technology with<br>Confidence and Independence</h2>

  <div class="scene-art" role="img" aria-label="Illustration of an older couple sitting together on a sofa using a laptop, with houseplants and a side table"></div>

  <svg class="books-badge" viewBox="0 0 104 104" role="img" aria-label="Books available on site">
    <circle cx="52" cy="52" r="52" fill="#2f4f2a"/>
    <circle cx="52" cy="52" r="47" fill="none" stroke="#fbf7f2" stroke-width="1" stroke-dasharray="3 2.5"/>
    <text x="52" y="38">BOOKS</text>
    <text x="52" y="58">AVAILABLE</text>
    <text x="52" y="78">ON SITE</text>
  </svg>

  <div class="details">
    <div class="detail-row" style="top:14px"><span class="detail-label">Location:</span><span class="detail-fill"></span></div>
    <div class="detail-row" style="top:44px"><span class="detail-label">Dates:</span><span class="detail-fill" style="top:10px"></span></div>
    <div class="detail-row" style="top:73px"><span class="detail-label">Time:</span><span class="detail-fill" style="top:8px"></span></div>
    <div class="detail-row" style="top:101px"><span class="detail-label">Cost:</span><span class="detail-value">$20 per session or $80 for full series (Pay at the door • No registration required)To ensure a seat register at QR Code and URL</span></div>
    <div class="detail-row" style="top:160px"><span class="detail-label">Format:</span><span class="detail-value" style="left:72px;top:3px">In-person • relaxed • community-focused</span></div>
  </div>

  <h3 class="testimonials-heading">What Participants Are Saying</h3>

  <figure class="quote" style="left:408px;top:703px">
    <blockquote class="quote-box">Very enjoyable.<br>I am learning a lot</blockquote>
    <svg class="quote-mark" viewBox="0 0 33 33" aria-hidden="true"><circle cx="16.5" cy="16.5" r="16.5" fill="#e0622d"/><text x="16.5" y="27" text-anchor="middle" font-family="Libre Caslon Text, serif" font-weight="700" font-size="26" fill="#fbf7f2">“</text></svg>
  </figure>
  <figure class="quote" style="left:589px;top:703px">
    <blockquote class="quote-box">Loved the anecdotes<br>and real-life examples</blockquote>
    <svg class="quote-mark" viewBox="0 0 33 33" aria-hidden="true"><circle cx="16.5" cy="16.5" r="16.5" fill="#e0622d"/><text x="16.5" y="27" text-anchor="middle" font-family="Libre Caslon Text, serif" font-weight="700" font-size="26" fill="#fbf7f2">“</text></svg>
  </figure>
  <figure class="quote" style="left:408px;top:782px">
    <blockquote class="quote-box" style="padding-top:7px">Excellent speaker.<br>Great pace and very<br>approachable.</blockquote>
    <svg class="quote-mark" viewBox="0 0 33 33" aria-hidden="true"><circle cx="16.5" cy="16.5" r="16.5" fill="#e0622d"/><text x="16.5" y="27" text-anchor="middle" font-family="Libre Caslon Text, serif" font-weight="700" font-size="26" fill="#fbf7f2">“</text></svg>
  </figure>
  <figure class="quote" style="left:589px;top:782px">
    <blockquote class="quote-box" style="padding-top:10px">I am a 90-year-old<br>reluctant learner and<br>I really enjoyed it.</blockquote>
    <svg class="quote-mark" viewBox="0 0 33 33" aria-hidden="true"><circle cx="16.5" cy="16.5" r="16.5" fill="#e0622d"/><text x="16.5" y="27" text-anchor="middle" font-family="Libre Caslon Text, serif" font-weight="700" font-size="26" fill="#fbf7f2">“</text></svg>
  </figure>

  <section class="presenter">
    <div class="presenter-text">
      <p class="presenter-name">Presented by Daniel Marwood</p>
      <p class="presenter-bio">technology expert, consultant, with over 40 years of technology experience and knowledge. Daniel keeps up to date with current technology and trends. He has helped thousands of adults build confidence with technology through clear, practical, and supportive learning experiences</p>
    </div>
  </section>
  <div class="presenter-photo" role="img" aria-label="Portrait photo of the presenter in a dark blazer with arms crossed"></div>
</main>
</body>
</html>
```